Locksmith Business Cards

My father-in-law is in need of new business cards for his locksmith business and I need to impress him. Kindly help me out!

You can see the previous business card attached. It is a family run business in North Wales.

No individual names on the cards.

Key Things to Feature:
- The words "Prompt", "Local", "Reliable" (as you can see under the logo on the website)
- 24h Emergency Service
- Covering All of North Wales, the Wirral and Chester
- The color blue
- A key or a lock would be interesting (similar to the ones that come up when you google locksmith business card)

Optional (only if design includes bullet points, like the example below):
https://imgvaultcdnx.net/design_img/318264/57190/57190_2749031_318264_image.jpg
- Residential / Commercial / Automotive
- Alarms & Cameras
- Key Cutting & Safes

https://www.bryncoed-locksmiths-demo.co.uk/

Locksmith

01632 960 418
07700 900 362
bryncoedlocksmiths@mailvalex.com
Bryncoed Locksmiths, Hafod Barn, 4 Pennant Rd., Llandudno LL39 7QZ
www.bryncoed-locksmiths-demo.co.uk

• - The words "Prompt", "Local", "Reliable" (as you can see under the logo on the website)
• - 24h Emergency Service
• - Covering All of North Wales, the Wirral and Chester
• - A key or a lock would be interesting (similar to the ones that come up when you google locksmith business card)

```html
<!DOCTYPE html>
<html lang="en">
<head>
<meta charset="utf-8">
<title>Bryncoed Locksmiths – Business Card</title>
<link rel="stylesheet" href="https://fonts.googleapis.com/css2?family=Oswald:wght@500&family=Roboto:wght@400;500&display=swap">
<style>
  :root {
    --backdrop: #3a3a3c;
    --navy: #2b3170;
    --navy-deep: #262b63;
    --periwinkle: #6c7fc1;
    --brand-blue: #3e4b9a;
    --ink: #3b3b3f;
    --paper: #ffffff;
    --white: #ffffff;
  }
  * { box-sizing: border-box; margin: 0; padding: 0; }
  html, body {
    width: 1200px; height: 900px; overflow: hidden;
    background: var(--backdrop);
    font-family: "Roboto", Arial, sans-serif;
  }
  .stage {
    position: relative; width: 1200px; height: 900px;
  }
  .card {
    position: absolute; left: 270px;
    width: 660px; height: 377px;
    border-radius: 4px;
    box-shadow: 0 14px 30px rgba(0,0,0,.45);
    overflow: hidden;
  }
  /* Front */
  .card--front {
    top: 52px;
    background: linear-gradient(125deg, var(--navy-deep) 0%, var(--navy) 40%, var(--periwinkle) 100%);
    color: var(--white);
    text-align: center;
  }
  .front__name {
    position: absolute; left: 0; right: 0; top: 92px;
    font-family: "Oswald", "Arial Narrow", sans-serif;
    font-weight: 500; font-size: 46px; line-height: 1.05;
    letter-spacing: 1px; text-transform: uppercase;
  }
  .front__tagline {
    position: absolute; left: 0; right: 0; top: 236px;
    font-size: 17px; line-height: 1.3; letter-spacing: .3px;
  }
  .front__tagline .values { letter-spacing: 1.5px; }

  /* Back */
  .card--back {
    top: 470px;
    background: var(--paper);
  }
  .back__name {
    position: absolute; left: 44px; top: 30px;
    font-family: "Oswald", "Arial Narrow", sans-serif;
    font-weight: 500; font-size: 30px; line-height: 1.05;
    color: var(--brand-blue); text-transform: uppercase; letter-spacing: .5px;
  }
  .services {
    position: absolute; left: 44px; top: 112px;
    list-style: none; color: var(--ink);
    font-size: 17px; line-height: 1.35;
  }
  .divider {
    position: absolute; left: 44px; top: 214px;
    width: 460px; height: 1.5px; background: var(--brand-blue);
  }
  .contacts {
    position: absolute; left: 44px; top: 236px;
    list-style: none; color: var(--ink);
    font-size: 18px; line-height: 1.6;
  }
  .contacts li { display: flex; align-items: center; gap: 10px; }
  .contacts svg { width: 18px; height: 18px; fill: var(--brand-blue); flex: none; }
  .address {
    position: absolute; right: 40px; top: 214px;
    text-align: right; color: var(--brand-blue);
    font-size: 18px; line-height: 1.35;
    font-style: normal;
  }
</style>
</head>
<body>
<main class="stage">

  <section class="card card--front" aria-label="Business card front">
    <h1 class="front__name">Bryncoed<br>Locksmiths</h1>
    <p class="front__tagline">
      <span class="values">PROMPT - LOCAL - RELIABLE</span><br>
      24h Emergency Service<br>
      Covering All of North Wales, the Wirral and Chester
    </p>
  </section>

  <section class="card card--back" aria-label="Business card back">
    <h2 class="back__name">Bryncoed<br>Locksmiths</h2>
    <ul class="services">
      <li>Residential | Commercial | Automotive</li>
      <li>Alarms &amp; Cameras</li>
      <li>Key Cutting &amp; Safes</li>
    </ul>
    <div class="divider"></div>
    <ul class="contacts">
      <li>
        <svg viewBox="0 0 24 24" aria-hidden="true"><path d="M6.6 10.8a15.1 15.1 0 0 0 6.6 6.6l2.2-2.2c.3-.3.7-.4 1-.2 1.1.4 2.3.6 3.6.6.6 0 1 .4 1 1V20c0 .6-.4 1-1 1A17 17 0 0 1 3 4c0-.6.4-1 1-1h3.5c.6 0 1 .4 1 1 0 1.3.2 2.5.6 3.6.1.3 0 .7-.2 1z"/></svg>
        01632 960 418
      </li>
      <li>
        <svg viewBox="0 0 24 24" aria-hidden="true"><path d="M6.6 10.8a15.1 15.1 0 0 0 6.6 6.6l2.2-2.2c.3-.3.7-.4 1-.2 1.1.4 2.3.6 3.6.6.6 0 1 .4 1 1V20c0 .6-.4 1-1 1A17 17 0 0 1 3 4c0-.6.4-1 1-1h3.5c.6 0 1 .4 1 1 0 1.3.2 2.5.6 3.6.1.3 0 .7-.2 1z"/></svg>
        07700 900 362
      </li>
      <li>
        <svg viewBox="0 0 24 24" aria-hidden="true"><path d="M2 5h20v14H2z M2 5l10 8 10-8" fill="none" stroke="#3e4b9a" stroke-width="2"/></svg>
        bryncoedlocksmiths@mailvalex.com
      </li>
      <li>
        <svg viewBox="0 0 24 24" aria-hidden="true"><g fill="none" stroke="#3e4b9a" stroke-width="1.8"><circle cx="12" cy="12" r="9.5"/><ellipse cx="12" cy="12" rx="4" ry="9.5"/><path d="M2.5 12h19"/></g></svg>
        www.bryncoed-locksmiths-demo.co.uk
      </li>
    </ul>
    <address class="address">
      Hafod Barn, 4, Pennant Rd.<br>
      Llandudno LL39 7QZ
    </address>
  </section>

</main>
</body>
</html>
```